indépendant en tant que Massothérapeute et Préparateur Mental, j'ai besoin de ...

Massothérapeute et préparateur mental indépendant, je recherche une carte de visite sobre et dynamique, sans images liées au massage ou à la préparation mentale mais intégrant mon logo. Les couleurs que j'aime bien sont : Blanc, gris, anthracite, noir et jaune

Contact Information for Business Card

carte de préférence Horizontale
neutre qui puisse toucher le deux domaines Massothérapie et préparation mentale

Requirements
Must have
• mon projet doit intégrer au recto:
LOGO
Loïc Vermande
078 315 26 49
info@loicvermande-exemple.ch
et éventuellement www.loicvermande-exemple.ch

et au verso les deux adresses:

Chemin des Ormelets 27B
1400 Yverdon-les-Bains

Rue des Tanneries 9
1700 Fribourg

Should not have
• mon projet ne doit pas contenir d'image en liens avec le massage ni la préparation mentale.

```html
<!DOCTYPE html>
<html lang="fr">
<head>
<meta charset="utf-8">
<title>Loïc Vermande – Carte de visite</title>
<link rel="stylesheet" href="https://fonts.googleapis.com/css2?family=Jost:wght@400;500;600&display=swap">
<style>
  :root {
    --yellow: #ebb30a;
    --paper: #f1efea;
    --ink: #262a33;
    --grey: #4a4e57;
    --backdrop: #e6e3dc;
    --white: #ffffff;
  }
  * { box-sizing: border-box; margin: 0; padding: 0; }
  html, body { width: 1200px; height: 878px; overflow: hidden; }
  body {
    background: var(--backdrop);
    font-family: "Jost", "Helvetica Neue", Arial, sans-serif;
    display: flex;
    align-items: center;
    justify-content: center;
    gap: 60px;
  }
  .card {
    width: 520px;
    height: 300px;
    position: relative;
    box-shadow: 0 6px 18px rgba(0,0,0,0.12);
  }
  .card--front { background: var(--paper); }
  .card--back { background: var(--yellow); color: var(--white); }

  .brand { position: absolute; }
  .brand__name {
    font-size: 24px;
    font-weight: 500;
    letter-spacing: 0.5px;
    display: flex;
    align-items: center;
    gap: 8px;
  }
  .brand__dot { width: 10px; height: 10px; border-radius: 50%; background: currentColor; }
  .brand__tagline {
    font-size: 7.5px;
    font-weight: 500;
    letter-spacing: 1px;
    text-transform: uppercase;
    margin-top: 4px;
    padding-left: 18px;
  }
  .card--front .brand { left: 34px; top: 186px; color: var(--yellow); }
  .card--back .brand { right: 32px; bottom: 34px; color: var(--white); }

  .divider {
    position: absolute;
    left: 282px; top: 58px;
    width: 1px; height: 150px;
    background: var(--yellow);
  }
  .identity { position: absolute; left: 302px; top: 62px; color: var(--ink); }
  .identity__name {
    font-size: 21px;
    font-weight: 600;
    letter-spacing: 1.5px;
    text-transform: uppercase;
    margin-bottom: 18px;
  }
  .contact { list-style: none; }
  .contact li {
    display: flex;
    align-items: center;
    gap: 8px;
    font-size: 12px;
    color: var(--grey);
    margin-bottom: 6px;
  }
  .contact svg { width: 10px; height: 10px; fill: var(--yellow); flex: none; }

  .addresses { position: absolute; left: 40px; top: 52px; list-style: none; }
  .addresses li {
    display: flex;
    align-items: flex-start;
    gap: 12px;
    font-size: 15px;
    line-height: 1.25;
    margin-bottom: 18px;
  }
  .addresses svg { width: 14px; height: 18px; fill: var(--white); margin-top: 8px; flex: none; }
</style>
</head>
<body>
  <section class="card card--front" aria-label="Recto">
    <div class="brand">
      <div class="brand__name"><span class="brand__dot"></span>Loïc Vermande</div>
      <div class="brand__tagline">Massothérapeute / Préparateur Mental</div>
    </div>
    <div class="divider"></div>
    <div class="identity">
      <h1 class="identity__name">Loïc Vermande</h1>
      <ul class="contact">
        <li><svg viewBox="0 0 10 10"><path d="M2 0.5 L4 2.5 L3 4 Q4.5 6 6 7 L7.5 6 L9.5 8 L8 9.5 Q3 9 0.5 2 Z"/></svg>078 315 26 49</li>
        <li><svg viewBox="0 0 10 10"><path d="M0 2 H10 V8 H0 Z M0.5 2.5 L5 5.8 L9.5 2.5" stroke="#f1efea" stroke-width="0.8"/></svg>info@loicvermande-exemple.ch</li>
        <li><svg viewBox="0 0 10 10"><circle cx="5" cy="5" r="4.5"/><path d="M0.5 5 H9.5 M5 0.5 V9.5" stroke="#f1efea" stroke-width="0.7"/></svg>www.loicvermande-exemple.ch</li>
      </ul>
    </div>
  </section>

  <section class="card card--back" aria-label="Verso">
    <ul class="addresses">
      <li><svg viewBox="0 0 14 18"><path d="M7 0 A7 7 0 0 1 14 7 C14 12 7 18 7 18 C7 18 0 12 0 7 A7 7 0 0 1 7 0 Z M7 4.5 A2.5 2.5 0 1 0 7 9.5 A2.5 2.5 0 1 0 7 4.5 Z" fill-rule="evenodd"/></svg><span>Chemin des Ormelets 27B<br>1400 Yverdon-les-Bains</span></li>
      <li><svg viewBox="0 0 14 18"><path d="M7 0 A7 7 0 0 1 14 7 C14 12 7 18 7 18 C7 18 0 12 0 7 A7 7 0 0 1 7 0 Z M7 4.5 A2.5 2.5 0 1 0 7 9.5 A2.5 2.5 0 1 0 7 4.5 Z" fill-rule="evenodd"/></svg><span>Rue des Tanneries 9<br>1700 Freiburg</span></li>
    </ul>
    <div class="brand">
      <div class="brand__name"><span class="brand__dot"></span>Loïc Vermande</div>
      <div class="brand__tagline">Massothérapeute / Préparateur Mental</div>
    </div>
  </section>
</body>
</html>
```